Book Cover for Productivity Book

I need a book cover for my latest publication "On Momentum: The Gathered Insights of the Busiest Woman Living"

You can see my branding at www.brightmarrow.example

This is meant to be my epic pinaccle work on productivity, I want it to look like the end all be all word on productivity.

Target Market(s)

entrepreneurs

```html
<!DOCTYPE html>
<html lang="en">
<head>
<meta charset="utf-8">
<title>On Momentum — Book Cover</title>
<link href="https://fonts.googleapis.com/css2?family=Saira+Condensed:wght@800&display=swap" rel="stylesheet">
<style>
  :root {
    --backdrop-light: #efefef;
    --backdrop-dark: #cbcbcb;
    --cover-yellow: #f8c655;
    --cover-ink: #1b1b1b;
  }
  html, body {
    margin: 0;
    padding: 0;
    width: 1200px;
    height: 900px;
    overflow: hidden;
  }
  body {
    background: radial-gradient(ellipse at 50% 50%, var(--backdrop-light) 0%, var(--backdrop-dark) 100%);
    position: relative;
  }
  .book-cover {
    position: absolute;
    left: 333px;
    top: 29px;
    width: 534px;
    height: 834px;
    display: block;
  }
  .cover-text {
    font-family: "Saira Condensed", "Arial Narrow", sans-serif;
    font-weight: 800;
    text-transform: uppercase;
  }
  .ink { fill: var(--cover-ink); }
  .gold { fill: var(--cover-yellow); }
</style>
</head>
<body>
  <svg class="book-cover" viewBox="0 0 534 834" role="img" aria-label="On Momentum: The Gathered Insights of the Busiest Woman Living">
    <rect class="gold" x="0" y="0" width="534" height="834"/>
    <polygon class="ink" points="260,449 534,640 534,834 0,834 0,640"/>

    <text class="cover-text ink series-line" x="267" y="122" font-size="51" text-anchor="middle" textLength="330" lengthAdjust="spacingAndGlyphs">On Momentum</text>
    <text class="cover-text ink title-lead" x="267" y="242" font-size="77" text-anchor="middle" textLength="449" lengthAdjust="spacingAndGlyphs">The Gathered</text>
    <text class="cover-text ink title-key" x="267" y="353" font-size="140" text-anchor="middle" textLength="449" lengthAdjust="spacingAndGlyphs">Insights</text>
    <text class="cover-text ink title-join" x="267" y="433" font-size="101" text-anchor="middle" textLength="250" lengthAdjust="spacingAndGlyphs">Of The</text>

    <text class="cover-text gold subject-line" x="267" y="661" font-size="60" text-anchor="middle" textLength="365" lengthAdjust="spacingAndGlyphs">Busiest</text>
    <text class="cover-text gold subject-name" x="267" y="737" font-size="91" text-anchor="middle" textLength="365" lengthAdjust="spacingAndGlyphs">Woman Living</text>
  </svg>
</body>
</html>
```